Patriotic Coffee Label

Design a 4"x6" (1200 px x 1800 px) portrait coffee label with a patriotic (USA) feel. The label must include a logo and include a military image. A sample logo and image will be attached. The final files must include .psd (preferred) or .ai templates with layers accessible.

DO NOT place your label on a mock up of a coffee bag! I only need the label design.

If you are the selected winner, you agree to complete the attached Copyright Transfer Agreement.pdf

Document setup:
Artboard: 4 x 6 inches
Color Mode: CMYK
Raster Effects: 300 PPI
Bleed: 0 / none
Output: JPEG, 1200 x 1800px, maximum quality; but .psd or .ai files must be provided with all layers editable.
Design: Edge to edge, background elements fill to artboard boundary

Typefaces: primary is Whitney, for web Whitney Book or Whitney Light for body text, Whitney Semibold, Whitney Bold or Whitney Black for heading. Alternates are Nunito Sans (Google Fonts / Adobe Fonts).
Colors: There are brand colors: old glory blue CMYK 100/87/37/51, old glory red CMYK 8/100/77/1 abd white CMYK 0/0/0/0. Sedondary color is blue CMYK 100/45/0/45 and should represent 20% or less of color usage. Images are exempt, they will be full color, but other elements should follow this guideline. Tertiary colors includ military green, coyote brown, olive, tan sand charcoal, light gray.

Imagery: use provided image, however, the image may be styled in any manner to fit your design vision. Image should be a smart object so that it can be substituted for a similar military image.

Note that other patriotic imagery (US flag) or military symbols can be incorporated as long as they are available in the public domain or you can release copyright.

Design elements that should be included in your design:
1. Logo
2. Name - use "Bramblewood Coffee"
3. Imagery and/or background design
4. Regulatory block - leave bottom 1" clear for regulatory text on readable background.

```html
<!DOCTYPE html>
<html lang="en">
<head>
<meta charset="utf-8">
<title>Bramblewood Coffee Label</title>
<link rel="stylesheet" href="https://fonts.googleapis.com/css2?family=Nunito+Sans:wght@400;600;700;800&display=swap">
<style>
  :root {
    --glory-blue: #0b2147;
    --glory-red: #bc1540;
    --white: #ffffff;
    --ink: #111111;
    --ornament-tint: #c9d0dc;
  }
  html, body {
    margin: 0;
    padding: 0;
    overflow: hidden;
    background: var(--white);
  }
  .label {
    position: relative;
    width: 800px;
    height: 1200px;
    overflow: hidden;
    background: var(--white);
    font-family: "Nunito Sans", sans-serif;
  }
  .brand-band {
    position: absolute;
    left: 295px;
    top: 0;
    width: 210px;
    height: 300px;
    background: var(--glory-red);
  }
  .brand-name {
    position: absolute;
    left: 295px;
    top: 90px;
    width: 210px;
    text-align: center;
    font-weight: 800;
    font-size: 58px;
    line-height: 1;
    color: var(--white);
    letter-spacing: 1px;
  }
  .badge {
    position: absolute;
    left: 0;
    top: 0;
    width: 800px;
    height: 1200px;
  }
  .badge-text {
    position: absolute;
    left: 0;
    width: 800px;
    text-align: center;
    color: var(--glory-blue);
  }
  .tagline { top: 440px; font-size: 31px; font-weight: 400; }
  .product-name {
    top: 525px;
    font-weight: 700;
    line-height: 1;
  }
  .product-name .first { display: block; color: var(--glory-red); font-size: 74px; }
  .product-name .second { display: block; color: var(--glory-blue); font-size: 88px; margin-top: 6px; }
  .since { top: 762px; font-size: 31px; font-weight: 400; }
  .weight { top: 824px; font-size: 21px; font-weight: 400; }
  .regulatory {
    position: absolute;
    left: 55px;
    top: 1004px;
    width: 690px;
    color: var(--ink);
  }
  .regulatory h2 {
    margin: 0 0 4px;
    text-align: center;
    font-size: 23px;
    font-weight: 700;
  }
  .regulatory p {
    margin: 0;
    font-size: 17px;
    line-height: 24.5px;
    text-align: justify;
    text-align-last: center;
  }
</style>
</head>
<body>
<div class="label">
  <div class="brand-band"></div>
  <div class="brand-name">Valor</div>

  <svg class="badge" width="800" height="1200" viewBox="0 0 800 1200">
    <circle class="badge-ring-outer" cx="400" cy="613" r="333" fill="var(--white)" stroke="var(--glory-blue)" stroke-width="16"/>
    <circle class="badge-ring-inner" cx="400" cy="613" r="305" fill="none" stroke="var(--glory-blue)" stroke-width="5"/>
    <g class="corner-ornaments">
      <circle cx="200" cy="410" r="62" fill="var(--ornament-tint)" role="img" aria-label="Leaf and scroll ornament"/>
      <circle cx="600" cy="410" r="62" fill="var(--ornament-tint)" role="img" aria-label="Leaf and scroll ornament"/>
      <circle cx="200" cy="816" r="62" fill="var(--ornament-tint)" role="img" aria-label="Leaf and scroll ornament"/>
      <circle cx="600" cy="816" r="62" fill="var(--ornament-tint)" role="img" aria-label="Leaf and scroll ornament"/>
    </g>
    <path class="divider" d="M337 498 Q400 494 463 498 Q400 502 337 498 Z" fill="var(--glory-blue)" stroke="var(--glory-blue)" stroke-width="2"/>
    <path class="divider" d="M337 749 Q400 745 463 749 Q400 753 337 749 Z" fill="var(--glory-blue)" stroke="var(--glory-blue)" stroke-width="2"/>
  </svg>

  <div class="badge-text tagline">100% Natural</div>
  <h1 class="badge-text product-name" style="margin:0">
    <span class="first">Bramblewood</span>
    <span class="second">Coffee</span>
  </h1>
  <div class="badge-text since">SINCE 2022</div>
  <div class="badge-text weight">250gr</div>

  <section class="regulatory">
    <h2>REGULATORY TEXT</h2>
    <p>Lorem ipsum dolor sit amet, consectetuer adipiscing elit, sed diam nonummy nibh euismod tincidunt ut laoreet dolore magna aliquam erat volutpat. Ut wisi enim ad minim veniam, quis nostrud exerci tation ullamcorper suscipit lobortis nisl ut aliquip ex ea commodo consequat. blandit praesent luptatum zzril delenit augue duis dolore te feugait nulla facilisi.</p>
  </section>
</div>
</body>
</html>
```